Software company needs a web design

We need a web design for the main page of our company, called Brixel Software (where Brixel goes for Brisk Pixel Firm). We develop and sell software for SME as well as Corporate sector within whole European continent.
Our main products are now OVN 7, an (real estate) asset management software enabling efficient management of commercial real estates; DUNE, software for loan management and two HR applications.
As our philosophy is efficiency, focusing on substance, getting rid of cumulated ballast etc., we'd like the web showing the same, i.e. being simple intuitive, rather visual then having too much text but still presenting our products (and our company via them) properly.
People visiting the web should easily find the right information on the company, people behind and our products as well as getting the right impression on what we aim to.
Attached is our company logo.

```html
<!DOCTYPE html>
<html lang="en">
<head>
<meta charset="UTF-8">
<title>Brixel Software</title>
<link rel="stylesheet" href="https://fonts.googleapis.com/css2?family=Fira+Sans:wght@400;700;900&family=Fira+Sans+Condensed:wght@900&family=Libre+Baskerville:wght@700&display=swap">
<style>
  :root {
    --navy: #2d3160;
    --blue: #4390d0;
    --blue-light: #5fb6e2;
    --blue-deep: #3a86c8;
    --red: #ea535d;
    --white: #ffffff;
    --page: #f3f5fa;
    --card: #fcfcfd;
  }
  * { margin: 0; padding: 0; box-sizing: border-box; }
  html, body { width: 1200px; height: 1200px; overflow: hidden; }
  body { position: relative; background: var(--page); font-family: "Fira Sans", sans-serif; }

  .site-header { position: absolute; top: 0; left: 0; width: 1200px; height: 108px; background: var(--blue); }
  .brand-panel { position: absolute; inset: 0; }
  .brand-name {
    position: absolute; left: 133px; top: 30px;
    font-family: "Fira Sans", sans-serif; font-weight: 400; font-size: 39px;
    color: var(--navy); letter-spacing: 0.2px; white-space: nowrap;
  }
  .main-nav { position: absolute; top: 34px; left: 619px; display: flex; align-items: center; }
  .nav-link {
    font-weight: 700; font-size: 18px; color: var(--white); text-decoration: none;
    height: 44px; line-height: 44px; margin-right: 30px;
  }
  .nav-link.is-active { background: var(--red); border-radius: 22px; padding: 0 23px; margin-right: 22px; }

  .hero { position: absolute; top: 108px; left: 0; width: 1200px; height: 644px; overflow: hidden; }
  .hero-backdrop { position: absolute; inset: 0; background: linear-gradient(110deg, var(--blue-light) 0%, #56a9dc 55%, var(--blue-deep) 100%); }
  .hero-device { position: absolute; left: 0; top: 0; }
  .hero-title {
    position: absolute; left: 132px; top: 128px;
    font-family: "Fira Sans Condensed", sans-serif; font-weight: 900; font-size: 142px;
    line-height: 1; color: var(--red); letter-spacing: -3px; white-space: nowrap;
    text-shadow: 3px 3px 0 var(--white), 6px 8px 14px rgba(20,50,100,.25);
  }
  .hero-subtitle {
    position: absolute; left: 133px; top: 276px; width: 470px;
    font-weight: 700; font-size: 29px; line-height: 38px; color: var(--white);
    white-space: nowrap;
    text-shadow: 2px 2px 0 rgba(30,60,120,.55);
  }
  .install-btn {
    position: absolute; left: 134px; top: 441px; width: 344px; height: 89px;
    border: 8px solid var(--white); border-radius: 45px; background: var(--blue);
    font-family: "Libre Baskerville", serif; font-weight: 700; font-size: 29px;
    color: var(--white); text-align: center; line-height: 73px; text-decoration: none;
    box-shadow: 0 10px 20px rgba(20,60,120,.25);
  }

  .apps-heading {
    position: absolute; top: 860px; left: 0; width: 1200px; text-align: center;
    font-family: "Libre Baskerville", serif; font-weight: 700; font-size: 55px;
    color: var(--navy); letter-spacing: 0.5px;
  }
  .app-card {
    position: absolute; background: var(--card); border-radius: 26px;
    box-shadow: 0 12px 40px rgba(40,60,110,.08);
  }
  .app-card.side-left { left: 132px; top: 1056px; width: 320px; height: 200px; }
  .app-card.side-right { left: 749px; top: 1056px; width: 320px; height: 200px; }
  .app-card.featured { left: 410px; top: 989px; width: 380px; height: 260px; border: 1px solid #e6e9f1; }
  .app-icon { position: absolute; border-radius: 6px; }
</style>
</head>
<body>
  <header class="site-header">
    <svg class="brand-panel" width="1200" height="108" viewBox="0 0 1200 108" aria-hidden="true">
      <polygon points="0,0 520,0 548,108 0,108" fill="#ffffff"/>
    </svg>
    <div class="brand-name">Brixel Software</div>
    <nav class="main-nav">
      <a class="nav-link is-active" href="#">HOME</a>
      <a class="nav-link" href="#">APPLICATIONS</a>
      <a class="nav-link" href="#">ABOUT</a>
      <a class="nav-link" href="#">CONTACT</a>
    </nav>
  </header>

  <section class="hero">
    <div class="hero-backdrop" role="img" aria-label="Blue-tinted photo of a bright lounge with armchairs and palm plants"></div>
    <svg class="hero-device" width="1200" height="644" viewBox="0 0 1200 644" role="img" aria-label="Tablet showing photos of a modern apartment interior">
      <defs>
        <linearGradient id="deviceFill" x1="0" y1="0" x2="1" y2="1">
          <stop offset="0" stop-color="#c9ccc8"/>
          <stop offset="0.55" stop-color="#b59a7a"/>
          <stop offset="1" stop-color="#8a6a4c"/>
        </linearGradient>
      </defs>
      <polygon points="554,185 985,85 1182,374 760,527" fill="url(#deviceFill)" opacity="0.95"/>
    </svg>
    <h1 class="hero-title">OVN 7</h1>
    <p class="hero-subtitle">Asset management software<br>enabling efficient management<br>of commercial real estates</p>
    <a class="install-btn" href="#">INSTALL APP</a>
  </section>

  <h2 class="apps-heading">MEET OUR APPS:</h2>

  <div class="app-card side-left">
    <div class="app-icon" style="left:90px;top:68px;width:120px;height:80px;background:linear-gradient(135deg,#7fa7c9,#e86a8a);" role="img" aria-label="Dashboard app illustration"></div>
  </div>
  <div class="app-card side-right">
    <div class="app-icon" style="left:117px;top:66px;width:105px;height:80px;background:linear-gradient(135deg,#4d8fe0,#a2d34a);" role="img" aria-label="Chat bubbles with two people illustration"></div>
  </div>
  <div class="app-card featured">
    <div class="app-icon" style="left:110px;top:43px;width:161px;height:140px;background:linear-gradient(180deg,#f3b12a 0%,#8ccd3f 60%,#e2b486 100%);" role="img" aria-label="Illustration of three stylised trees"></div>
  </div>
</body>
</html>
```